Kestrel Homes Web Site Design

improve on the graphic design on our current website
www.kestrelhmoes.com.au
wordpress required

Industry/Entity Type

Graphic Design

Coding

Coded - Design and coding required

Number of Pages Required

5+ page

```html
<!DOCTYPE html>
<html lang="en">
<head>
<meta charset="utf-8">
<title>Kestrel Homes</title>
<link href="https://fonts.googleapis.com/css2?family=Raleway:wght@400;600;700;800&family=Open+Sans:wght@400;600;700&display=swap" rel="stylesheet">
<style>
:root{
  --red:#a5121c;
  --red-dark:#8a0e16;
  --slate:#4b4a4e;
  --slate-dark:#3f3e42;
  --ink:#2b2a2d;
  --footer:#2e2c2d;
  --paper:#ececec;
  --white:#ffffff;
  --text:#555;
  --muted:#888;
}
*{box-sizing:border-box;margin:0;padding:0}
html,body{width:1200px;height:4018px;overflow:hidden}
body{font-family:"Open Sans",Arial,sans-serif;color:var(--text);background:var(--white);position:relative}
.wrap{width:932px;margin:0 auto;position:relative}
h2.section-title{font-family:"Raleway",Arial,sans-serif;font-weight:800;font-size:22px;color:var(--red);text-align:center;letter-spacing:.5px}
h2.section-title.light{color:var(--white)}
.section-title::after{content:"";display:block;width:40px;height:2px;background:var(--red);margin:10px auto 0}
.btn{display:inline-block;background:var(--red);color:var(--white);font-family:"Raleway",Arial,sans-serif;font-weight:700;text-transform:uppercase;letter-spacing:.5px}

/* hero */
.hero{position:relative;height:536px;overflow:hidden}
.hero-photo{position:absolute;inset:0;background:linear-gradient(180deg,#a9b1ba 0%,#8b96a2 45%,#55606c 75%,#2c3036 100%)}
.topbar{position:absolute;right:0;top:0;height:34px;width:420px;background:rgba(20,20,22,.85);display:flex;align-items:center;justify-content:flex-end;padding-right:136px;gap:12px;color:var(--white)}
.topbar .phone{font-weight:700;font-size:15px;display:flex;align-items:center;gap:6px}
.topbar .follow{font-size:11px;color:#ccc;margin-left:10px}
.dot-social{width:20px;height:20px;border-radius:50%;background:var(--red)}
.side-nav{position:absolute;left:129px;top:32px;width:260px;height:437px;background:rgba(25,25,27,.88);padding:24px 30px}
.brand{font-family:"Raleway",Arial,sans-serif;font-weight:800;font-size:30px;color:var(--white);display:flex;align-items:center;gap:10px}
.brand .mark{width:20px;height:20px;border-radius:50%;background:var(--red)}
.side-nav ul{list-style:none;margin-top:36px}
.side-nav li{font-size:14px;color:#ddd;padding:11px 0 11px 18px;border-bottom:1px solid rgba(255,255,255,.12);position:relative}
.side-nav li::before{content:"";position:absolute;left:0;top:17px;width:6px;height:6px;background:var(--red);border-radius:50%}
.side-nav .btn{font-size:12px;padding:10px 16px;margin-top:22px}
.slide-text{position:absolute;left:718px;top:330px;color:var(--white)}
.slide-text h1{font-family:"Raleway",Arial,sans-serif;font-weight:800;font-size:46px;letter-spacing:.5px}
.slide-text p{font-size:17px;margin-top:4px}
.slide-text .btn{font-size:14px;padding:12px 24px;margin-top:18px}
.arrow{position:absolute;top:273px;width:48px;height:48px;border-radius:50%;background:rgba(20,20,20,.8)}
.arrow.prev{left:62px}.arrow.next{right:62px}
.arrow svg{position:absolute;inset:14px}

/* features */
.features{height:389px;padding-top:27px}
.features .wrap{display:flex;justify-content:space-between}
.feature{width:300px;text-align:center}
.feature .photo{height:214px;position:relative}
.feature .badge{position:absolute;left:50%;bottom:-40px;margin-left:-42px;width:84px;height:84px;border-radius:50%;background:var(--white);border:5px solid var(--red);display:flex;align-items:center;justify-content:center}
.feature h3{font-family:"Raleway",Arial,sans-serif;font-weight:800;font-size:15px;color:var(--ink);margin-top:52px}
.feature p{font-size:12px;line-height:1.5;margin-top:8px;padding:0 14px}

/* why */
.why{height:388px;background:var(--slate);color:#ddd}
.why .wrap{padding-top:52px}
.why h2{font-family:"Raleway",Arial,sans-serif;font-weight:800;font-size:24px;color:var(--white)}
.why p{font-size:13px;line-height:1.6;width:470px;margin-top:18px}
.stats{display:flex;gap:60px;margin-top:34px}
.stat{display:flex;align-items:center;gap:18px}
.stat .ring{width:84px;height:84px;border-radius:50%;background:var(--white);display:flex;align-items:center;justify-content:center}
.stat b{display:block;font-family:"Raleway",Arial,sans-serif;font-weight:800;font-size:30px;color:var(--red)}
.stat span{font-size:12px;font-weight:700;color:var(--white);text-transform:uppercase}
.why-brand{position:absolute;right:0;top:110px;width:310px;height:180px;display:flex;align-items:center;justify-content:center;gap:14px;font-family:"Raleway",Arial,sans-serif;font-weight:800;font-size:40px;color:var(--white)}
.why-brand .mark{width:40px;height:40px;border-radius:50%;background:var(--red)}

/* portfolio */
.portfolio{height:630px;background:var(--paper);padding-top:38px}
.filters{display:flex;justify-content:center;gap:6px;margin-top:26px}
.filters span{font-size:11px;font-weight:600;text-transform:uppercase;padding:8px 12px;background:var(--white);border:1px solid #ccc;color:#444}
.filters span.active{background:var(--red);color:var(--white);border-color:var(--red)}
.grid{display:grid;grid-template-columns:repeat(3,300px);grid-auto-rows:206px;gap:16px;margin-top:24px;justify-content:space-between}
.tile{position:relative}
.tile .cap{position:absolute;left:14px;bottom:12px;color:var(--white)}
.tile .cap b{font-family:"Raleway",Arial,sans-serif;font-weight:800;font-size:14px;display:block}
.tile .cap span{font-size:12px}

/* team */
.team{height:456px;padding-top:50px}
.members{display:flex;justify-content:space-between;margin-top:34px;padding:0 20px}
.member{width:195px;text-align:center}
.member .portrait{width:195px;height:195px;border-radius:50%}
.member h4{font-family:"Raleway",Arial,sans-serif;font-weight:800;font-size:13px;color:var(--red-dark);margin-top:22px}
.member small{display:block;font-size:11px;color:#333;margin-top:2px}
.member .btn{font-size:10px;padding:5px 10px;margin-top:12px}

/* testimonials */
.testimonials{height:464px;background:var(--slate-dark);padding-top:42px}
.quotes{display:flex;justify-content:space-between;margin-top:40px}
.quote{width:456px;height:289px;background:var(--slate);box-shadow:0 2px 8px rgba(0,0,0,.35);padding:26px 28px;position:relative;color:#ddd}
.quote .mark{position:absolute;left:26px;top:22px}
.quote h4{font-family:"Raleway",Arial,sans-serif;font-weight:800;font-size:15px;color:var(--white);margin-left:66px;line-height:1.4}
.quote p{font-size:12px;line-height:1.65;margin:16px 0 0 66px}
.author{display:flex;align-items:center;gap:14px;margin:18px 0 0 0}
.author .avatar{width:44px;height:44px;background:linear-gradient(135deg,#9a8f86,#5f5a56)}
.author b{font-size:11px;color:var(--white);display:block}
.author .stars{color:#e89b1a;font-size:12px;letter-spacing:1px}

/* contact */
.contact{height:627px;background:var(--paper);padding-top:46px}
.contact-grid{display:flex;justify-content:space-between;margin-top:42px}
.contact-left{width:504px}
.address-card{height:129px;background:var(--white);display:flex;padding:20px 24px;gap:30px}
.address-card .brand{color:var(--ink);font-size:22px}
.address-card dl{font-size:12px;color:#444;display:grid;grid-template-columns:auto auto;gap:4px 40px}
.address-card dt{font-weight:700;color:var(--red);font-size:12px}
.map{height:322px;margin-top:13px;background:linear-gradient(135deg,#d8dcc9,#c4cdbf 50%,#d6d2c2)}
.form{width:401px}
.field{height:46px;background:var(--white);margin-bottom:8px;font-size:12px;color:#666;padding:14px 12px}
.field.message{height:132px}
.send{height:56px;background:var(--red);color:var(--white);font-family:"Raleway",Arial,sans-serif;font-weight:800;font-size:20px;display:flex;align-items:center;justify-content:center;margin-top:10px}

/* cta */
.cta{height:209px;text-align:center;padding-top:60px}
.cta p{font-family:"Raleway",Arial,sans-serif;font-size:24px;color:var(--red)}
.cta p b{font-weight:800}
.cta .btn{font-size:15px;padding:16px 30px;margin-top:20px}

/* footer */
.footer{height:319px;background:var(--footer);color:#ccc;position:relative}
.footer .brand{position:absolute;left:134px;top:84px;font-size:36px}
.footer .brand .mark{width:26px;height:26px}
.foot-col{position:absolute;top:70px}
.foot-col h5{font-family:"Raleway",Arial,sans-serif;font-weight:800;font-size:12px;color:var(--white);text-transform:uppercase;margin-bottom:8px;line-height:1.4}
.foot-col li{list-style:none;font-size:11px;line-height:1.65}
.foot-col.menu{left:472px}.foot-col.services{left:608px}.foot-col.discover{left:764px;width:300px}
.nums{display:flex;gap:12px;margin-top:12px}
.nums span{width:36px;height:36px;border-radius:50%;border:2px solid var(--white);background:var(--red);color:var(--white);font-weight:700;font-size:13px;display:flex;align-items:center;justify-content:center}
.follow-us{position:absolute;left:134px;bottom:40px;display:flex;align-items:center;gap:8px;font-size:11px;color:var(--white)}
.follow-us .lbl{margin-right:14px}
.follow-us i{width:16px;height:16px;border-radius:50%;background:#3b5ea8}
.follow-us i:nth-child(3){background:#2ea3dc}.follow-us i:nth-child(4){background:var(--red)}.follow-us i:nth-child(5){background:#1f6fae}
.copyright{position:absolute;right:134px;bottom:40px;font-size:10px;color:#888}
</style>
</head>
<body>

<header class="hero">
  <div class="hero-photo" role="img" aria-label="Photo of a tall glass office tower against a cloudy sky"></div>
  <div class="topbar">
    <span class="phone"><svg width="14" height="14" viewBox="0 0 24 24"><path fill="#fff" d="M6.6 10.8a15 15 0 0 0 6.6 6.6l2.2-2.2c.3-.3.7-.4 1-.2 1.1.4 2.3.6 3.6.6.6 0 1 .4 1 1V20c0 .6-.4 1-1 1A17 17 0 0 1 3 4c0-.6.4-1 1-1h3.5c.6 0 1 .4 1 1 0 1.2.2 2.4.6 3.6.1.3 0 .7-.2 1z"/></svg>0400 318 562</span>
    <span class="follow">Follow us</span>
    <span class="dot-social"></span><span class="dot-social"></span><span class="dot-social"></span>
  </div>
  <nav class="side-nav">
    <div class="brand"><span class="mark"></span>Kestrel</div>
    <ul>
      <li>Home</li><li>About Us</li><li>Excellence</li><li>Experience</li><li>Expertise</li><li>Contact</li>
    </ul>
    <span class="btn">See our gallery</span>
  </nav>
  <div class="arrow prev"><svg width="20" height="20" viewBox="0 0 20 20"><path d="M13 3 6 10l7 7" stroke="#fff" stroke-width="2.5" fill="none"/></svg></div>
  <div class="arrow next"><svg width="20" height="20" viewBox="0 0 20 20"><path d="M7 3l7 7-7 7" stroke="#fff" stroke-width="2.5" fill="none"/></svg></div>
  <div class="slide-text">
    <h1>ARCHITECTURE</h1>
    <p>Lorem ipsum is simply dummy text of the printing</p>
    <span class="btn">Learn more ›</span>
  </div>
</header>

<section class="features">
  <div class="wrap">
    <article class="feature">
      <div class="photo" role="img" aria-label="Photo of a government building with a flagpole" style="background:linear-gradient(180deg,#3f7fd0,#8fb4e0 60%,#c9c7c0)">
        <div class="badge"><svg width="40" height="40" viewBox="0 0 40 40"><path d="M6 18 20 7l14 11v15H6z" fill="none" stroke="#2b2a2d" stroke-width="3"/><rect x="16" y="23" width="8" height="10" fill="#a5121c"/></svg></div>
      </div>
      <h3>CANBERRA BUILDING</h3>
      <p>Kestrel Homes is a Canberra based building company focusing on first class residential homes and 100% client satisfaction.</p>
    </article>
    <article class="feature">
      <div class="photo" role="img" aria-label="Photo of modern glass office towers" style="background:linear-gradient(180deg,#a8c4e4,#5c7ea8 60%,#3a4d66)">
        <div class="badge"><svg width="40" height="40" viewBox="0 0 40 40"><path d="M8 32 32 8M8 8l24 24" stroke="#2b2a2d" stroke-width="3"/><circle cx="20" cy="20" r="5" fill="#a5121c"/></svg></div>
      </div>
      <h3>TOP CLASS ARCHITECTS</h3>
      <p>Working with the best architects in Canberra, has always been our strength. This ensures our ability to deliver home designs tailored to your specific requirements.</p>
    </article>
    <article class="feature">
      <div class="photo" role="img" aria-label="Photo of construction workers on a site at sunset" style="background:linear-gradient(180deg,#e9a25a,#c3682f 55%,#3a2a2a)">
        <div class="badge"><svg width="40" height="40" viewBox="0 0 40 40"><path d="M7 26a13 13 0 0 1 26 0z" fill="#2b2a2d"/><rect x="4" y="26" width="32" height="5" fill="#a5121c"/></svg></div>
      </div>
      <h3>RELIABLE CONTRACTORS</h3>
      <p>Working with the best contractors in the industry enables us to provide you with construction services that are on time and on budget.</p>
    </article>
  </div>
</section>

<section class="why">
  <div class="wrap">
    <h2>WHY KESTREL HOMES?</h2>
    <p>Our vision is to build homes to the highest standards. We're a boutique building company in Canberra, that has built many residential properties.</p>
    <p>Being in the industry for many years has enabled us to master the art of designing and constructing stylish homes that are not only aesthetically pleasing but also affordable.</p>
    <div class="stats">
      <div class="stat"><div class="ring"><svg width="44" height="44" viewBox="0 0 44 44"><circle cx="22" cy="14" r="7" fill="none" stroke="#a5121c" stroke-width="3"/><path d="M8 38c0-8 6-13 14-13s14 5 14 13" fill="none" stroke="#a5121c" stroke-width="3"/></svg></div><div><b>18+</b><span>People in our team</span></div></div>
      <div class="stat"><div class="ring"><svg width="44" height="44" viewBox="0 0 44 44"><g fill="#a5121c"><rect x="6" y="10" width="14" height="7"/><rect x="23" y="10" width="15" height="7"/><rect x="6" y="19" width="7" height="7"/><rect x="15" y="19" width="14" height="7"/><rect x="31" y="19" width="7" height="7"/><rect x="6" y="28" width="14" height="7"/><rect x="23" y="28" width="15" height="7"/></g></svg></div><div><b>253</b><span>Houses we built</span></div></div>
    </div>
    <div class="why-brand"><span class="mark"></span>Kestrel Homes</div>
  </div>
</section>

<section class="portfolio">
  <div class="wrap">
    <h2 class="section-title">PORTFOLIO</h2>
    <div class="filters"><span class="active">All</span><span>Gallery</span><span>Builder</span><span>Extensions</span><span>Bathrooms</span><span>Refurbishment</span></div>
    <div class="grid">
      <div class="tile" role="img" aria-label="Photo of a glass office building at dusk" style="background:linear-gradient(160deg,#27447a,#4f77b8 55%,#1b2740)"><div class="cap"><b>HEADING 1</b><span>Lorem ipsum is simply dummy text of the</span></div></div>
      <div class="tile" role="img" aria-label="Photo of a lit modern house at night" style="background:linear-gradient(160deg,#1b1f2a,#3b3a40 50%,#b07a3e)"><div class="cap"><b>HEADING 2</b><span>Lorem ipsum is simply dummy text of the</span></div></div>
      <div class="tile" role="img" aria-label="Photo of high-rise towers under blue sky" style="background:linear-gradient(160deg,#8fb6e2,#4f7fbf 55%,#2a3f60)"><div class="cap"><b>HEADING 3</b><span>Lorem ipsum is simply dummy text of the</span></div></div>
      <div class="tile" role="img" aria-label="Photo of a white angular building" style="background:linear-gradient(160deg,#6f8fb8,#c8ccd4 55%,#586478)"><div class="cap"><b>HEADING 4</b><span>Lorem ipsum is simply dummy text of the</span></div></div>
      <div class="tile" role="img" aria-label="Photo of an apartment block with lit windows" style="background:linear-gradient(160deg,#3b5fa8,#6b88c6 50%,#2b2e48)"><div class="cap"><b>HEADING 5</b><span>Lorem ipsum is simply dummy text of the</span></div></div>
      <div class="tile" role="img" aria-label="Photo of a curved residential tower" style="background:linear-gradient(160deg,#b9cde4,#7a98bd 55%,#4a5a70)"><div class="cap"><b>HEADING 6</b><span>Lorem ipsum is simply dummy text of the</span></div></div>
    </div>
  </div>
</section>

<section class="team">
  <div class="wrap">
    <h2 class="section-title">TEAM</h2>
    <div class="members">
      <div class="member"><div class="portrait" role="img" aria-label="Portrait photo of a team member" style="background:radial-gradient(circle,#bdbdbd,#4a4a4a)"></div><h4>DAMON KELLER</h4><small>CEO &amp; ARCHITECT</small><span class="btn">View bio</span></div>
      <div class="member"><div class="portrait" role="img" aria-label="Portrait photo of a team member" style="background:radial-gradient(circle,#b8b8b8,#3e3e3e)"></div><h4>LENA MARSH</h4><small>ARCHITECT</small><span class="btn">View bio</span></div>
      <div class="member"><div class="portrait" role="img" aria-label="Portrait photo of a team member" style="background:radial-gradient(circle,#c9c9c9,#555)"></div><h4>DAMON KELLER</h4><small>CEO &amp; ARCHITECT</small><span class="btn">View bio</span></div>
      <div class="member"><div class="portrait" role="img" aria-label="Portrait photo of a team member" style="background:radial-gradient(circle,#c2c2c2,#444)"></div><h4>DAMON KELLER</h4><small>CEO &amp; ARCHITECT</small><span class="btn">View bio</span></div>
    </div>
  </div>
</section>

<section class="testimonials">
  <div class="wrap">
    <h2 class="section-title light">TESTIMONIALS</h2>
    <div class="quotes">
      <article class="quote">
        <svg class="mark" width="48" height="38" viewBox="0 0 48 38"><path d="M0 38V20C0 8 6 1 18 0v7c-6 1-9 5-9 11h9v20zm26 0V20C26 8 32 1 44 0v7c-6 1-9 5-9 11h9v20z" fill="#8a898c"/></svg>
        <h4>Knowledge is knowledge whether it teaches you construction or destruction</h4>
        <p>I've engaged Kestrel Homes to build my first house in Canberra, all I can say is they've been fantastic. Tom has helped me out at every stage of the building process, making sure everything was handled smoothly. Whenever I needed a change they've been very helpful.</p>
        <div class="author"><div class="avatar" role="img" aria-label="Small portrait photo of the client"></div><div><b>CLARA DENHOLM</b><span class="stars">★★★★★</span></div></div>
      </article>
      <article class="quote">
        <svg class="mark" width="48" height="38" viewBox="0 0 48 38"><path d="M0 38V20C0 8 6 1 18 0v7c-6 1-9 5-9 11h9v20zm26 0V20C26 8 32 1 44 0v7c-6 1-9 5-9 11h9v20z" fill="#8a898c"/></svg>
        <h4>There are many variations of passages of Lorem Ipsum available.</h4>
        <p>It uses a dictionary of over 200 Latin words, combined with a handful of model sentence structures, to generate Lorem Ipsum which looks reasonable. The generated Lorem Ipsum is therefore always free from repetition, injected humour, or non-characteristic words etc.</p>
        <div class="author"><div class="avatar" role="img" aria-label="Small portrait photo of the client"></div><div><b>OWEN HALE</b><span class="stars">★★★★★</span></div></div>
      </article>
    </div>
  </div>
</section>

<section class="contact">
  <div class="wrap">
    <h2 class="section-title">GET IN TOUCH</h2>
    <div class="contact-grid">
      <div class="contact-left">
        <div class="address-card">
          <div class="brand"><span class="mark"></span>Kestrel</div>
          <dl>
            <dt>ADDRESS :</dt><dt></dt>
            <dd>14 Harlow Street, Eastbrook</dd><dd></dd>
            <dt>TEL :</dt><dt>E-mail</dt>
            <dd>0400 318 562</dd><dd>info@kestrelhomes.com.au</dd>
          </dl>
        </div>
        <div class="map" role="img" aria-label="Street map showing the office location"></div>
      </div>
      <form class="form">
        <div class="field">Name</div>
        <div class="field">Phone</div>
        <div class="field">E-mail</div>
        <div class="field">Required work:</div>
        <div class="field">When would you like us to call you?</div>
        <div class="field message">Message</div>
        <div class="send">SEND</div>
      </form>
    </div>
  </div>
</section>

<section class="cta">
  <p>Get a <b>FREE</b> building estimation today for your next project!</p>
  <span class="btn">Get me the quote</span>
</section>

<footer class="footer">
  <div class="brand"><span class="mark"></span>Kestrel</div>
  <div class="foot-col menu"><h5>Menu</h5><ul><li>Home</li><li>Company</li><li>Excellence</li><li>Experience</li><li>Expertise</li><li>Contact</li></ul></div>
  <div class="foot-col services"><h5>Services</h5><ul><li>General builder</li><li>House extensions</li><li>Refurbishment</li><li>Electricity</li><li>Bathrooms</li><li>Kitchens</li></ul></div>
  <div class="foot-col discover"><h5>Discover the reason that make us better<br>value than our competitors</h5><div class="nums"><span>1</span><span>2</span><span>3</span><span>4</span></div></div>
  <div class="follow-us"><span class="lbl">FOLLOW US ON</span><i></i><i></i><i></i><i></i></div>
  <div class="copyright">Copyrights © 2015 All Rights Reserved</div>
</footer>

</body>
</html>
```